Venture Traps Book Needs a Cover Design

We need a cover design for Venture Traps, Plain Guidance for Wobbly New Ventures and Stalled Company Founders. We will publish and ebook first (first priority), followed by a hard cover printed book, and then a soft cover book after a few months. The book includes 40 Venture Traps and actions owners can implement to counter them and grow. Some examples of killers: self-sabotage, wild optimism, scamming, addictions, burnout, no plan, procrastination, recklessness, haemorrhaging money, etc. We plan to publish the ebook to Readlo / Vendora standards. We want to see designs that convey professionalism, simplicity and creativity.

Target Market(s)

Small and microbusinesses, including start-ups, proprietorships, cottage industries, home-based, single operator, and businesses with or without employees, including corporations and partnerships with fewer than five employees

Industry/Entity Type

Business

Font styles to use
Sans Serif

Colors

Designer to choose colors to be used in the design.

Requirements
Must have
• Uncluttered, professional
• Title: Venture Traps
• Subtitle: Plain Guidance for Wobbly New Ventures and Stalled Company Founders
• Author: Miles Farquist
Nice to have
• n/a

```html
<!DOCTYPE html>
<html lang="en">
<head>
<meta charset="utf-8">
<title>Venture Traps — Book Cover</title>
<link rel="stylesheet" href="https://fonts.googleapis.com/css2?family=Bebas+Neue&family=Barlow+Condensed:wght@600&family=Cinzel:wght@400&display=swap">
<style>
  :root {
    --page: #ffffff;
    --navy-top: #07163a;
    --navy-bottom: #1c3362;
    --title-red: #e5191f;
    --band-red: #d41c22;
    --subtitle-cream: #fdf0a0;
    --author-band: #33497f;
    --author-white: #ffffff;
    --name-yellow: #fbf59a;
    --glow-light: rgba(214, 224, 255, 0.55);
    --glow-fade: rgba(214, 224, 255, 0);
  }
  * { margin: 0; padding: 0; box-sizing: border-box; }
  html, body {
    width: 1200px; height: 1200px; overflow: hidden;
    background: var(--page);
  }
  .canvas { position: relative; width: 1200px; height: 1200px; }
  .book-cover {
    position: absolute; left: 409px; top: 297px;
    width: 373px; height: 560px; overflow: hidden;
  }
  .cover-sky {
    position: absolute; left: 0; top: 0; width: 373px; height: 305px;
    background: linear-gradient(180deg, var(--navy-top) 0%, var(--navy-bottom) 100%);
  }
  .spark-artwork {
    position: absolute; left: 160px; top: 4px; width: 210px; height: 116px;
    background: radial-gradient(ellipse 45% 55% at 75% 45%, var(--glow-light) 0%, var(--glow-fade) 100%);
  }
  .book-title {
    position: absolute; left: 0; top: 118px; width: 373px;
    text-align: center;
    font-family: "Bebas Neue", "Arial Narrow", sans-serif;
    font-weight: 400;
    font-size: 110px; line-height: 86px; letter-spacing: 2px;
    color: var(--title-red);
  }
  .subtitle-band {
    position: absolute; left: 0; top: 305px; width: 373px; height: 170px;
    background: var(--band-red);
    display: flex; align-items: center; justify-content: center;
  }
  .book-subtitle {
    text-align: center;
    font-family: "Barlow Condensed", "Arial Narrow", sans-serif;
    font-weight: 600; font-size: 34px; line-height: 38.5px;
    text-transform: uppercase; color: var(--subtitle-cream);
  }
  .author-band {
    position: absolute; left: 0; top: 475px; width: 373px; height: 85px;
    background: var(--author-band);
    display: flex; align-items: center; justify-content: center;
  }
  .book-author {
    font-family: "Barlow Condensed", "Arial Narrow", sans-serif;
    font-weight: 600; font-size: 56px; line-height: 1;
    text-transform: uppercase; color: var(--author-white);
  }
  .author-name-display {
    position: absolute; left: 273px; top: 1044px; width: 510px;
    text-align: center;
    font-family: "Cinzel", Georgia, serif;
    font-size: 62px; line-height: 1; white-space: nowrap;
    color: var(--name-yellow);
  }
</style>
</head>
<body>
<div class="canvas">
  <div class="book-cover">
    <div class="cover-sky"></div>
    <div class="spark-artwork" role="img" aria-label="Artwork: a lit fuse with a glowing spark above the title"></div>
    <h1 class="book-title">Venture<br>Traps</h1>
    <div class="subtitle-band">
      <p class="book-subtitle">Plain Guidance for<br>Wobbly New Ventures<br>and Stalled Company<br>Founders</p>
    </div>
    <div class="author-band">
      <p class="book-author">Miles Farquist</p>
    </div>
  </div>
  <p class="author-name-display">MILES FARQUIST</p>
</div>
</body>
</html>
```